Unique Concept Design to Website Needed

Please see the attached folder. I have random images,etc but most importantly I have an attached image I was working on as a concept of a website. The brown background with blue and brown squares. logo in upper left and a little about me and then the squares would have names on them to lead to a section of the website with more info. I envision, when you mouse over a square, an image would appear so I attached random images here as well. Maybe some squares already have some images too.
- I want simple fonts. i like CLEAN, fonts
- text should be minimal. i am changing my site to less text, more powerful, bolder, larger lines with less content
- i am not sold on brown as the secondary color. i like blue but maybe grays, whites, offwhite scales or some other colors
-i have another graphic in there too
-you can see from my mock what company i am. please feel free to look me up and pull any portfolio , info , etc content to help make a great mock.
Do something cool!

```html
<!DOCTYPE html>
<html lang="en">
<head>
<meta charset="utf-8">
<title>Swiftline Web Studio — Welcome</title>
<link rel="stylesheet" href="https://fonts.googleapis.com/css2?family=Open+Sans:wght@400;600;700&display=swap">
<style>
  :root {
    --blue: #41b4fb;
    --gray: #a3a3a3;
    --gray-dark: #9c9c9c;
    --gray-light: #cbcbcb;
    --faint-blue: #e8f5fe;
    --faint-gray: #f1f1f1;
    --brand: #4a7aa3;
    --tagline: #8a9aa8;
    --paper: #ffffff;
    --photo-dark: #3c3c3c;
    --photo-light: #b8b8b8;
    --r: 42px;
    --r-small: 18px;
  }
  * { box-sizing: border-box; margin: 0; padding: 0; }
  html, body { width: 1200px; height: 1200px; overflow: hidden; background: var(--paper); }
  body { font-family: "Open Sans", Arial, sans-serif; }
  .canvas { position: relative; width: 1200px; height: 1200px; overflow: hidden; background: var(--paper); }

  /* faint background tile clusters */
  .faint-cluster { position: absolute; display: grid; grid-template-columns: repeat(6, 48px); grid-auto-rows: 48px; gap: 2px; }
  .faint-cluster span { background: var(--faint-gray); }
  .faint-cluster span.b { background: var(--faint-blue); }
  .faint-cluster span.none { background: transparent; }
  .faint-cluster span.tl { border-top-left-radius: var(--r-small); }
  .faint-cluster span.tr { border-top-right-radius: var(--r-small); }
  .faint-cluster span.bl { border-bottom-left-radius: var(--r-small); }
  .faint-cluster span.br { border-bottom-right-radius: var(--r-small); }

  /* brand */
  .brand { position: absolute; left: 77px; top: 370px; width: 360px; }
  .brand-name { font-size: 25px; font-weight: 400; color: var(--brand); line-height: 1.1; white-space: nowrap; }
  .brand-tagline { margin-top: 10px; font-size: 11.5px; color: var(--tagline); letter-spacing: 0.2px; white-space: nowrap; }

  /* small header tiles */
  .mini { position: absolute; width: 49px; height: 49px; }
  .mini.dark { background: var(--gray-dark); }
  .mini.blue { background: var(--blue); }
  .mini.light { background: var(--gray-light); }
  .mini.tl { border-top-left-radius: var(--r-small); }
  .mini.tr { border-top-right-radius: var(--r-small); }
  .mini.bl { border-bottom-left-radius: var(--r-small); }
  .mini.br { border-bottom-right-radius: var(--r-small); }

  .welcome-band { position: absolute; left: 456px; top: 203px; width: 350px; height: 42px; display: flex; gap: 2px; }
  .welcome-band span { flex: 1; background: var(--blue); color: var(--paper); font-weight: 600; font-size: 20px; display: flex; align-items: center; justify-content: center; }
  .welcome-band span:first-child { border-top-left-radius: 14px; border-bottom-left-radius: 14px; }
  .welcome-band span:last-child { border-top-right-radius: 14px; border-bottom-right-radius: 14px; }

  /* main tiles */
  .tile { position: absolute; width: 99px; height: 99px; }
  .tile.blue { background: var(--blue); }
  .tile.gray { background: var(--gray); }
  .tile.photo { background: linear-gradient(135deg, var(--photo-light), var(--photo-dark)); }
  .tile.tl { border-top-left-radius: var(--r); }
  .tile.tr { border-top-right-radius: var(--r); }
  .tile.bl { border-bottom-left-radius: var(--r); }
  .tile.br { border-bottom-right-radius: var(--r); }

  .about-label { display: flex; flex-direction: column; align-items: flex-end; justify-content: center; padding-right: 12px; color: var(--paper); font-weight: 700; font-size: 22px; line-height: 1.2; }
  .about-photo { position: absolute; left: 658px; top: 304px; width: 201px; height: 200px; }
</style>
</head>
<body>
<div class="canvas">

  <!-- faint background tiles -->
  <div class="faint-cluster" style="left:880px; top:27px;">
    <span class="tl"></span><span></span><span class="b"></span><span></span><span class="b tl"></span><span class="b tr"></span>
    <span></span><span></span><span class="b tl"></span><span class="b"></span><span></span><span></span>
    <span class="b"></span><span></span><span class="b"></span><span class="b"></span><span></span><span class="b"></span>
    <span class="none"></span><span></span><span class="b bl"></span><span class="b"></span><span class="bl"></span><span class="br"></span>
  </div>
  <div class="faint-cluster" style="left:760px; top:228px; grid-template-columns: repeat(5, 48px);">
    <span class="none"></span><span></span><span class="tr"></span><span class="b tl"></span><span class="b tr"></span>
    <span class="none"></span><span class="b"></span><span class="b"></span><span></span><span></span>
    <span class="none"></span><span></span><span class="b"></span><span class="b"></span><span class="b"></span>
    <span class="none"></span><span></span><span></span><span class="br"></span><span class="bl"></span>
  </div>
  <div class="faint-cluster" style="left:177px; top:730px;">
    <span class="none"></span><span class="none"></span><span class="b tl"></span><span class="b tr"></span><span class="none"></span><span class="none"></span>
    <span class="tl"></span><span></span><span class="b"></span><span class="b"></span><span class="tl"></span><span class="tr"></span>
    <span class="b"></span><span></span><span class="b"></span><span class="b"></span><span></span><span></span>
    <span></span><span class="b"></span><span class="b"></span><span></span><span></span><span class="br"></span>
    <span class="b bl"></span><span class="b"></span><span></span><span></span><span class="b bl"></span><span class="b br"></span>
  </div>
  <div class="faint-cluster" style="left:24px; top:982px;">
    <span class="tl"></span><span></span><span class="b tl"></span><span class="b"></span><span class="tl"></span><span class="tr"></span>
    <span class="b"></span><span></span><span class="b"></span><span class="b"></span><span></span><span></span>
    <span></span><span class="b"></span><span></span><span class="b"></span><span></span><span class="b"></span>
    <span class="b bl"></span><span></span><span class="b"></span><span></span><span class="b"></span><span class="b br"></span>
  </div>

  <!-- brand -->
  <div class="brand">
    <div class="brand-name">Swiftline Web Studio, llc</div>
    <div class="brand-tagline">Website Design. Website Support. Website Promotion.</div>
  </div>

  <!-- header mini tiles -->
  <div class="mini dark tl" style="left:456px; top:152px;"></div>
  <div class="mini dark tr" style="left:506px; top:152px;"></div>
  <div class="mini blue tl" style="left:557px; top:152px;"></div>
  <div class="mini blue tr" style="left:607px; top:152px;"></div>
  <div class="mini light tl" style="left:658px; top:152px;"></div>
  <div class="mini light tr" style="left:708px; top:152px;"></div>

  <div class="welcome-band">
    <span>w</span><span>e</span><span>l</span><span>c</span><span>o</span><span>m</span><span>e</span>
  </div>

  <div class="mini dark bl" style="left:456px; top:253px;"></div>
  <div class="mini dark br" style="left:506px; top:253px;"></div>
  <div class="mini blue bl" style="left:557px; top:253px;"></div>
  <div class="mini blue br" style="left:607px; top:253px;"></div>
  <div class="mini light bl" style="left:658px; top:253px;"></div>
  <div class="mini light br" style="left:708px; top:253px;"></div>

  <!-- block: top left -->
  <div class="tile blue tl" style="left:456px; top:304px;"></div>
  <div class="tile blue" style="left:557px; top:304px;"></div>
  <div class="tile blue bl" style="left:456px; top:404px;"></div>
  <div class="tile blue br" style="left:557px; top:404px;"></div>

  <!-- about us -->
  <div class="about-photo" role="img" aria-label="Black and white photo of the team working at desks in the office">
    <div class="tile photo tr" style="left:102px; top:0;"></div>
    <div class="tile photo tl" style="left:0; top:100px;"></div>
    <div class="tile photo br" style="left:102px; top:100px;"></div>
  </div>
  <div class="tile blue tl about-label" style="left:658px; top:304px;"><span>ABOUT</span><span>US</span></div>

  <!-- block: right -->
  <div class="tile blue tl" style="left:861px; top:404px;"></div>
  <div class="tile blue tr" style="left:963px; top:404px;"></div>
  <div class="tile gray tl" style="left:861px; top:504px;"></div>
  <div class="tile blue" style="left:963px; top:504px;"></div>

  <!-- rows 2-3 left -->
  <div class="tile blue tl" style="left:456px; top:504px;"></div>
  <div class="tile blue tr" style="left:557px; top:504px;"></div>
  <div class="tile gray tl" style="left:456px; top:604px;"></div>
  <div class="tile blue br" style="left:557px; top:604px;"></div>

  <!-- rows 2-3 center -->
  <div class="tile blue tl" style="left:658px; top:504px;"></div>
  <div class="tile blue tr" style="left:760px; top:504px;"></div>
  <div class="tile blue bl" style="left:658px; top:604px;"></div>
  <div class="tile blue br" style="left:760px; top:604px;"></div>

  <!-- rows 4-5 left -->
  <div class="tile gray tl" style="left:456px; top:705px;"></div>
  <div class="tile blue tr" style="left:557px; top:705px;"></div>
  <div class="tile blue bl" style="left:456px; top:805px;"></div>
  <div class="tile blue br" style="left:557px; top:805px;"></div>

  <!-- rows 4-7 center -->
  <div class="tile blue tl" style="left:658px; top:705px;"></div>
  <div class="tile blue tr" style="left:760px; top:705px;"></div>
  <div class="tile blue tl" style="left:658px; top:805px;"></div>
  <div class="tile gray tr" style="left:760px; top:805px;"></div>
  <div class="tile blue bl" style="left:861px; top:805px;"></div>
  <div class="tile blue" style="left:658px; top:907px;"></div>
  <div class="tile gray bl" style="left:760px; top:907px;"></div>
  <div class="tile blue tl" style="left:861px; top:907px;"></div>
  <div class="tile blue bl" style="left:658px; top:1007px;"></div>
  <div class="tile blue br" style="left:760px; top:1007px;"></div>

</div>
</body>
</html>
```